Graphic Design of Business Process

We require an eye-catching, sophisticated design of 2 business processes (attached), that will be used digitally AND for print (to be put on walls in our office).

The basic layout is attached. We require a creative, professional designer to re-design these so that they look appealing but still able to grasp all the information.

We will require vector files and editable project files for final delivery. You may refer to our website (kitefieldmedia.com.au) for an indication of our brand.

If you have any questions, please ask.

Thank you.

```html
<!DOCTYPE html>
<html lang="en">
<head>
<meta charset="utf-8">
<title>Content Hierarchy</title>
<link rel="stylesheet" href="https://fonts.googleapis.com/css2?family=Source+Code+Pro:wght@700&family=PT+Sans:wght@400&display=swap">
<style>
  :root {
    --bg: #d6d6d6;
    --navy: #344061;
    --pink: #f05373;
    --mint: #a2eed8;
    --white: #ffffff;
    --ink: #0b0b0f;
  }
  html, body {
    margin: 0;
    padding: 0;
    width: 1200px;
    height: 1200px;
    overflow: hidden;
    background: var(--bg);
  }
  .hierarchy {
    display: block;
    width: 1200px;
    height: 1200px;
  }
  .hierarchy__title {
    font-family: "Source Code Pro", monospace;
    font-weight: 700;
    font-size: 66px;
    fill: var(--navy);
  }
  .tier__name {
    font-family: "PT Sans", sans-serif;
    font-size: 56px;
    letter-spacing: 5px;
  }
  .tier__desc {
    font-family: "PT Sans", sans-serif;
    font-size: 31px;
    letter-spacing: 1.6px;
  }
  .pin__number {
    font-family: "PT Sans", sans-serif;
    font-size: 62px;
    letter-spacing: 1px;
  }
  .card--hero { fill: var(--white); }
  .card--hub { fill: var(--navy); }
  .card--hygiene { fill: var(--pink); }
  .text--navy { fill: var(--navy); }
  .text--ink { fill: var(--ink); }
  .text--pink { fill: var(--pink); }
  .pin__ring--navy { fill: var(--navy); }
  .pin__ring--pink { fill: var(--pink); }
  .pin__ring--mint { fill: var(--mint); }
  .pin__face { fill: var(--white); }
</style>
</head>
<body>
<svg class="hierarchy" viewBox="0 0 1200 1200" xmlns="http://www.w3.org/2000/svg">
  <text class="hierarchy__title" x="580" y="156" text-anchor="middle">CONTENT HIERARCHY</text>

  <!-- Tier 1: Hero -->
  <g class="tier tier--hero">
    <path class="card--hero" d="M342 309 H846 Q858 309 858 321 V525 H342 Z"/>
    <g class="pin">
      <circle class="pin__ring--navy" cx="427" cy="262" r="82"/>
      <path class="pin__ring--navy" d="M403 330 L451 330 L427 371 Z"/>
      <circle class="pin__face" cx="427" cy="262" r="59"/>
      <text class="pin__number text--pink" x="423" y="284" text-anchor="middle">01</text>
    </g>
    <text class="tier__name text--navy" x="467" y="376">HERO</text>
    <text class="tier__desc text--navy" x="371" y="428">TENTPOLE CAMPAIGNS</text>
  </g>

  <!-- Tier 2: Hub -->
  <g class="tier tier--hub">
    <path class="card--hub" d="M342 618 H846 Q858 618 858 630 V834 H342 Z"/>
    <g class="pin">
      <circle class="pin__ring--pink" cx="427" cy="570" r="82"/>
      <path class="pin__ring--pink" d="M403 638 L451 638 L427 680 Z"/>
      <circle class="pin__face" cx="427" cy="570" r="59"/>
      <text class="pin__number text--navy" x="423" y="592" text-anchor="middle">02</text>
    </g>
    <text class="tier__name text--ink" x="493" y="680">HUB</text>
    <text class="tier__desc text--ink" x="371" y="737">REGULAR “PUSH” CONTENT</text>
  </g>

  <!-- Tier 3: Hygiene -->
  <g class="tier tier--hygiene">
    <path class="card--hygiene" d="M342 926 H846 Q858 926 858 938 V1142 H342 Z"/>
    <g class="pin">
      <circle class="pin__ring--mint" cx="427" cy="878" r="82"/>
      <path class="pin__ring--mint" d="M403 946 L451 946 L427 989 Z"/>
      <circle class="pin__face" cx="427" cy="878" r="59"/>
      <text class="pin__number text--navy" x="423" y="900" text-anchor="middle">03</text>
    </g>
    <text class="tier__name text--ink" x="493" y="988">HYGIENE</text>
    <text class="tier__desc text--ink" x="371" y="1045">ALWAYS-ON “PULL”CONTENT</text>
  </g>
</svg>
</body>
</html>
```